New design of old website

We need a new design of our domain name reseller website.

kavirnodo.com

we would also like new design for Logo and all.

the site will be in English and portuguesse,

Domain

```html
<!DOCTYPE html>
<html lang="en">
<head>
<meta charset="utf-8">
<title>Kavirnodo – Domain Reseller</title>
<link rel="stylesheet" href="https://fonts.googleapis.com/css2?family=Arimo:wght@400;700&family=Open+Sans:wght@400;600&display=swap">
<style>
  :root {
    --teal: #62c3cc;
    --teal-deep: #129aa8;
    --teal-text: #3fb8c6;
    --teal-muted: #4a8d92;
    --heading-teal: #3e8a91;
    --cyan-band: #aef0f3;
    --tile-outer: #7de6f0;
    --tile-inner: #aef2f8;
    --tile-label: #1d5c63;
    --icon-grey: #7d9497;
    --ink: #000;
    --white: #fff;
  }
  * { box-sizing: border-box; margin: 0; padding: 0; }
  html, body { width: 1200px; height: 1000px; overflow: hidden; background: var(--white); }
  body { position: relative; font-family: "Arimo", Arial, sans-serif; color: var(--ink); }
  .abs { position: absolute; }

  .brand { left: 150px; top: 12px; display: flex; align-items: center; gap: 8px; }
  .brand-dot { width: 40px; height: 40px; border-radius: 50%; background: var(--teal); }
  .brand-name { font-family: "Open Sans", sans-serif; font-size: 30px; color: #1f2f33; }

  .search { left: 868px; top: 33px; width: 180px; height: 32px; background: #eaf8fa; box-shadow: 0 1px 3px rgba(0,0,0,.25); display: flex; align-items: center; padding-left: 6px; gap: 10px; font-size: 14px; color: var(--teal-deep); }

  .nav { left: 150px; top: 70px; width: 900px; height: 54px; background: var(--teal); border-radius: 8px; }
  .nav a { position: absolute; top: 0; height: 54px; line-height: 62px; font-family: "Open Sans", sans-serif; font-size: 16px; color: var(--white); text-decoration: none; word-spacing: 4px; }
  .nav .active { background: #000; left: 31px; width: 85px; text-align: center; }

  .hero { left: 150px; top: 124px; width: 900px; height: 331px; background: linear-gradient(#fff 0%, #e3f7f8 100%); }
  .hero-band { left: 0; top: 242px; width: 900px; height: 89px; background: var(--cyan-band); border-radius: 0 0 6px 6px; }
  .hero-photo { left: 330px; top: 16px; width: 550px; height: 300px; background: linear-gradient(#5b6268 0%, #2f3538 60%, rgba(174,240,243,.4) 100%); opacity: .85; border-radius: 4px; }
  .hero-title { left: 23px; top: 87px; font-family: "Open Sans", sans-serif; font-size: 22px; color: var(--heading-teal); }
  .hero-sub { left: 23px; top: 123px; font-family: "Open Sans", sans-serif; font-size: 17px; }
  .hero-link { left: 21px; top: 158px; font-family: "Open Sans", sans-serif; font-size: 16px; color: var(--heading-teal); text-decoration: underline; }
  .hero-shadow { left: 150px; top: 455px; width: 900px; height: 30px; background: linear-gradient(rgba(0,0,0,.12), rgba(0,0,0,0)); }

  .section-title { font-size: 22px; color: var(--teal-text); top: 476px; }
  .thumb { border: 3px solid #b8eef5; }
  .thumb-why { left: 184px; top: 510px; width: 306px; height: 130px; background: linear-gradient(#f4f7f7, #dfe8ea); }
  .thumb-services { left: 643px; top: 512px; width: 237px; height: 130px; background: linear-gradient(#e9ecec, #b9bfc1); }
  .lead { left: 183px; top: 665px; font-size: 17px; line-height: 20px; color: var(--teal-muted); }
  .copy { font-size: 15px; line-height: 18px; }
  .more { font-size: 12px; color: var(--teal-deep); text-decoration: underline; top: 814px; }

  .footer-rule { left: 0; top: 835px; width: 1200px; height: 4px; background: #000; }
  .features { left: 0; top: 839px; width: 1200px; height: 126px; background: var(--teal); }
  .tile { top: 9px; width: 199px; height: 107px; background: var(--tile-outer); border-radius: 8px; padding: 7px; }
  .tile-inner { width: 100%; height: 100%; background: var(--tile-inner); border-radius: 8px; text-align: center; padding-top: 6px; font-size: 14px; color: var(--tile-label); }
  .tile svg { display: block; margin: 4px auto 0; }
  .legal { left: 0; top: 965px; width: 1200px; height: 35px; background: var(--teal-deep); color: var(--white); font-size: 11px; text-align: center; line-height: 42px; }
</style>
</head>
<body>
  <header>
    <div class="abs brand"><span class="brand-dot"></span><span class="brand-name">kavirnodo</span></div>
    <div class="abs search">
      <svg width="20" height="20" viewBox="0 0 20 20"><circle cx="8" cy="8" r="6" fill="none" stroke="#6a8b90" stroke-width="2"/><line x1="12.5" y1="12.5" x2="18" y2="18" stroke="#6a8b90" stroke-width="2.5"/></svg>
      <span>Search..</span>
    </div>
    <nav class="abs nav">
      <a class="active" href="#">HOME</a>
      <a href="#" style="left:141px">WHY&nbsp; KAVIRNODO</a>
      <a href="#" style="left:294px">PRODUCTS</a>
      <a href="#" style="left:428px">SERVICES</a>
      <a href="#" style="left:554px">RESELLER</a>
      <a href="#" style="left:680px">CONTACT</a>
      <a href="#" style="left:801px">LOGIN</a>
    </nav>
  </header>

  <section class="abs hero">
    <div class="abs hero-band"></div>
    <div class="abs hero-photo" role="img" aria-label="Photo of a team of business people in suits walking forward"></div>
    <h1 class="abs hero-title" style="font-weight:400">LOCAL PRESENCE</h1>
    <p class="abs hero-sub">Everywhere you can count on us.</p>
    <a class="abs hero-link" href="#">The best solution for your business</a>
  </section>
  <div class="abs hero-shadow"></div>

  <section class="why">
    <h2 class="abs section-title" style="left:183px;font-weight:400">WHY KAVIRNODO</h2>
    <div class="abs thumb thumb-why" role="img" aria-label="Photo of a hand placing glass marbles in a row"></div>
    <p class="abs lead">Give your customers a choice of 250 Top<br>Level Domains (TLDs)</p>
    <p class="abs copy" style="left:183px;top:721px">Kavirnodo is mainly focused the the latin american marked.<br>Today Kavirnodo is the fastest growing .br registrar and today<br>many of the world's largest registrars are using Kavirnodo NIC<br>to register .br domain with or without local present.</p>
    <a class="abs more" href="#" style="left:533px">MORE</a>
  </section>

  <section class="services">
    <h2 class="abs section-title" style="left:641px;font-weight:400">OUR SERVICES</h2>
    <div class="abs thumb thumb-services" role="img" aria-label="Illustration of business people assembling giant puzzle pieces"></div>
    <p class="abs copy" style="left:642px;top:655px">Global WHOIS and Domain availability</p>
    <p class="abs copy" style="left:642px;top:691px">Access essential domain information across 250+ TLDs<br>Partner Portal</p>
    <p class="abs copy" style="left:642px;top:746px">A unified portal allowing you to perform every kind of<br>transaction through a single interface.</p>
    <a class="abs more" href="#" style="left:983px">MORE</a>
  </section>

  <footer>
    <div class="abs footer-rule"></div>
    <div class="abs features">
      <div class="abs tile" style="left:153px"><div class="tile-inner">Security
        <svg width="80" height="62" viewBox="0 0 80 62"><circle cx="22" cy="18" r="14" fill="#fff"/><circle cx="22" cy="18" r="5" fill="var(--tile-inner)"/><path d="M30 28 L66 58 L72 52 L66 47 L70 43 L64 38 L60 42 L36 22 Z" fill="#fff"/></svg></div></div>
      <div class="abs tile" style="left:384px"><div class="tile-inner">TLD Expecilist
        <svg width="130" height="62" viewBox="0 0 130 62"><circle cx="24" cy="22" r="11" fill="#4fb6d8"/><path d="M6 62 v-12 a18 14 0 0 1 36 0 v12z" fill="#4fb6d8"/><circle cx="106" cy="22" r="11" fill="#4fb6d8"/><path d="M88 62 v-12 a18 14 0 0 1 36 0 v12z" fill="#4fb6d8"/><circle cx="65" cy="14" r="14" fill="#3ed6ea"/><path d="M40 62 v-14 a25 18 0 0 1 50 0 v14z" fill="#3ed6ea"/></svg></div></div>
      <div class="abs tile" style="left:615px"><div class="tile-inner">Automation
        <svg width="110" height="62" viewBox="0 0 110 62"><g fill="none" stroke="var(--icon-grey)"><circle cx="40" cy="32" r="17" stroke-width="10" stroke-dasharray="7 4"/><circle cx="40" cy="32" r="10" stroke-width="4"/><circle cx="72" cy="30" r="19" stroke-width="10" stroke-dasharray="7 4"/><circle cx="72" cy="30" r="12" stroke-width="4"/></g></svg></div></div>
      <div class="abs tile" style="left:847px"><div class="tile-inner">Personal Service
        <svg width="80" height="62" viewBox="0 0 80 62"><g stroke="#6f7f80" stroke-width="9" stroke-linecap="round"><line x1="18" y1="8" x2="64" y2="58"/><line x1="62" y1="6" x2="20" y2="56"/></g><rect x="52" y="0" width="22" height="12" fill="#6f7f80" transform="rotate(-45 63 6)"/></svg></div></div>
    </div>
    <div class="abs legal">Copyrights © 2011 Lumen Studio</div>
  </footer>
</body>
</html>
```